Revamp Marketing Website For Video Production Website

need to revamp current website www.kelvaramediaclips.com
reference sites www.vintra.com & http://layoutquarry.com/kelvara/
Use all current content on current kelvara website. I want a revamped modenr look. Sometbing that wows customers.
reference site www.vintra.com
Updates
Target Market(s)
business owners
Industry/Entity Type
Video Production
Number of Pages Required
5+ page
Colors
Designer to choose colors to be used in the design.
Requirements
Must have
- need to revamp current website www.kelvaramediaclips.com
- reference sites www.vintra.com & http://layoutquarry.com/kelvara/
- Use all current content on current kelvara website. I want a revamped modenr look. Sometbing that wows customers.
- reference site www.vintra.com
Nice to have
Should not have

```html
<!DOCTYPE html>
<html lang="en">
<head>
<meta charset="utf-8">
<title>Kelvara – Marketing Videos Made For You</title>
<link href="https://fonts.googleapis.com/css2?family=Raleway:wght@300;400;500;600;700;800&display=swap" rel="stylesheet">
<style>
:root{
  --bg:#000000;
  --ink:#ffffff;
  --muted:#cfd3d8;
  --blue:#1e8cf0;
  --blue-light:#45aaff;
  --blue-deep:#136fd6;
  --panel:#0d1117;
}
*{margin:0;padding:0;box-sizing:border-box}
html,body{width:1200px;height:3403px;overflow:hidden;background:var(--bg)}
body{position:relative;font-family:'Raleway',sans-serif;color:var(--ink)}
.abs{position:absolute}
.center{left:0;width:1200px;text-align:center}

/* header */
.site-header{top:0;left:0;width:1200px;height:93px;background:#000;z-index:3}
.brand{left:234px;top:29px}
.brand-name{font-size:30px;font-weight:800;letter-spacing:3px;line-height:1;display:flex;align-items:center;gap:8px}
.brand-name i{display:inline-block;width:14px;height:14px;background:var(--blue)}
.brand-tag{font-size:8px;font-weight:600;letter-spacing:1px;margin-top:3px}
.main-nav{top:39px;left:456px;display:flex;gap:13px;font-size:11px;font-weight:700}
.login{top:39px;left:853px;font-size:11px;font-weight:700}
.btn{display:flex;align-items:center;justify-content:center;border-radius:20px;background:linear-gradient(180deg,var(--blue-light),var(--blue-deep));color:#fff;font-weight:700;box-shadow:0 0 0 2px rgba(255,255,255,.25)}
.signup{left:903px;top:31px;width:63px;height:30px;font-size:11px}

/* hero */
.hero{top:93px;left:0;width:1200px;height:462px;background:radial-gradient(ellipse 60% 55% at 50% 40%,#3a4146 0%,#23292d 45%,#0a0c0d 80%,#000 100%)}
.hero-title{top:212px;font-size:37px;font-weight:800}
.hero-sub{top:259px;font-size:21px;font-weight:700}
.hero-cta{left:476px;top:312px;width:248px;height:36px;font-size:15px}
.hero-note{top:359px;font-size:13px;font-style:italic;font-weight:300;color:var(--muted)}
.scroll-cue{left:586px;top:455px}

/* promote */
.promote-title{top:620px;font-size:29px;font-weight:800}
.promote-text{left:245px;width:710px;top:706px;font-size:14.5px;text-align:center;line-height:18px}
.we-create{left:234px;top:832px}
.we-create .hl{font-size:31px;font-weight:800;color:var(--blue);line-height:35px}
.we-create .lt{font-size:23px;font-weight:300;line-height:28px}
.social-ring{width:76px;height:76px;border:2.5px solid #fff;border-radius:50%}
.social-ring span{position:absolute;left:28px;top:28px;width:16px;height:16px;border-radius:50%;background:var(--blue)}

/* examples */
.examples{top:1070px;left:0;width:1200px;height:377px;background:radial-gradient(ellipse 55% 70% at 60% 40%,#2a3440 0%,#141a21 50%,#000 100%)}
.examples-ball{left:128px;top:1075px;width:320px;height:370px;border-radius:50%;background:radial-gradient(circle at 50% 40%,#3b3f44,#1b1d20 70%,transparent 72%)}
.section-title{font-size:29px;font-weight:800}
.thumb{top:1196px;width:220px;height:126px;overflow:hidden}
.thumb .play{position:absolute;left:96px;top:50px;width:28px;height:24px;background:rgba(0,0,0,.75);border-radius:3px}
.thumb .play:after{content:"";position:absolute;left:10px;top:6px;border-left:10px solid #fff;border-top:6px solid transparent;border-bottom:6px solid transparent}
.thumb .tool{position:absolute;right:6px;width:18px;height:18px;background:rgba(0,0,0,.75);border-radius:3px}
.small-btn{height:37px;font-size:11px;font-weight:700}

/* features */
.feature-ring{width:130px;height:130px;border:2.5px solid #fff;border-radius:50%;display:flex;align-items:center;justify-content:center}
.feature-label{width:260px;text-align:center;font-size:19px;font-weight:700;line-height:22px}

/* sizes */
.sizes-bg{top:2470px;left:0;width:1200px;height:570px;background:radial-gradient(ellipse 50% 60% at 70% 55%,#3a414a 0%,#1c2229 45%,#000 85%)}
.sizes-text{left:234px;width:731px;font-size:14.5px;line-height:18px}
.sizes-text b{font-weight:700}
.sizes-text .stars{color:var(--blue);font-weight:700;font-size:11px;vertical-align:top}
.frame{border:3px solid var(--blue);display:flex;align-items:center;justify-content:center;font-size:14px;font-weight:700}
.frame em{font-style:normal;color:var(--blue);margin:0 4px}

/* footer */
.footer-brand{left:234px;top:3272px}
.footer-brand .brand-name{font-size:34px}
.footer-credit{left:234px;top:3333px;font-size:11px;font-weight:700}
.foot-col{top:3247px;font-size:10.5px;font-weight:700;line-height:13.3px}
.foot-col h4{font-size:10.5px;font-weight:700;margin-bottom:14px}
.follow{display:flex;gap:11px;margin-top:0}
.follow span{width:12px;height:12px;border-radius:50%;background:var(--blue)}
.copyright{top:3392px;font-size:6px}
</style>
</head>
<body>

<header class="abs site-header">
  <div class="abs brand">
    <div class="brand-name"><i></i>KELVARA</div>
    <div class="brand-tag">MARKETING VIDEOS MADE FOR YOU</div>
  </div>
  <nav class="abs main-nav">
    <span>Home</span><span>How It Works</span><span>Examples</span><span>FAQ</span><span>Contact Us</span><span>Pricing</span>
  </nav>
  <span class="abs login">Log In</span>
  <span class="abs btn signup">Sign Up</span>
</header>

<section class="abs hero" role="img" aria-label="Curved wall of many glowing video screens"></section>
<h1 class="abs center hero-title">ATTENTION GRABBING VIDEO ADS</h1>
<p class="abs center hero-sub">DELIVERED IN 24 HOURS!</p>
<span class="abs btn hero-cta">Get One Free Mockup Now</span>
<p class="abs center hero-note">*No purchase necessary*</p>
<svg class="abs scroll-cue" width="28" height="48" viewBox="0 0 28 48" fill="none" stroke="#1e8cf0" stroke-width="2">
  <rect x="4" y="1" width="20" height="32" rx="10"/><line x1="14" y1="7" x2="14" y2="13"/><path d="M14 33v12M9 40l5 5 5-5"/>
</svg>

<h2 class="abs center promote-title">PROMOTE ANYTHING ANYWHERE ON THE WEB</h2>
<p class="abs promote-text">Still using static image ads with Pagestream, Lumigram, Workweave, Flashtalk advertising platforms? Turn them into VIDEO ADS and get higher conversion rates instantly.</p>

<div class="abs we-create">
  <div class="hl">We Create</div>
  <div class="lt">Award Winning Promotional</div>
  <div class="hl">Marketing Videos</div>
  <div class="lt">To Use All Over The Web</div>
</div>

<div class="abs social-ring" style="left:594px;top:805px"><span></span></div>
<div class="abs social-ring" style="left:742px;top:805px"><span></span></div>
<div class="abs social-ring" style="left:887px;top:805px"><span></span></div>
<div class="abs social-ring" style="left:594px;top:910px"><span></span></div>
<div class="abs social-ring" style="left:742px;top:910px"><span></span></div>
<div class="abs social-ring" style="left:887px;top:910px"><span></span></div>

<section class="abs examples" role="img" aria-label="Dark digital dashboard backdrop with charts and a laptop"></section>
<div class="abs examples-ball" role="img" aria-label="Hands typing on a laptop"></div>
<h2 class="abs center section-title" style="top:1105px">OUR EXAMPLES</h2>

<div class="abs thumb" style="left:234px" role="img" aria-label="Video thumbnail: business person in an office lobby">
  <div style="width:100%;height:100%;background:linear-gradient(135deg,#5d6e80,#2f3b49 60%,#8aa0b5)"></div>
  <div class="play"></div><div class="tool" style="top:6px"></div><div class="tool" style="top:30px"></div>
</div>
<div class="abs thumb" style="left:490px" role="img" aria-label="Video thumbnail: man in suit with flying money against concrete wall">
  <div style="width:100%;height:100%;background:linear-gradient(135deg,#7a7d80,#4c4f52 55%,#9a9c9e)"></div>
  <div class="play"></div><div class="tool" style="top:6px"></div><div class="tool" style="top:30px"></div>
</div>
<div class="abs thumb" style="left:747px" role="img" aria-label="Video thumbnail: dancer at a ballet barre in a bright studio">
  <div style="width:100%;height:100%;background:linear-gradient(135deg,#f0ece8,#d9d2cc 60%,#c9a9a5)"></div>
  <div class="play"></div><div class="tool" style="top:6px"></div><div class="tool" style="top:30px"></div>
</div>
<span class="abs btn small-btn" style="left:490px;top:1384px;width:220px">SHOW ALL CATECORY VIDEO</span>

<h2 class="abs center section-title" style="top:1539px">OUR FEATURES</h2>

<!-- row 1 -->
<div class="abs feature-ring" style="left:263px;top:1631px">
  <svg width="60" height="60" viewBox="0 0 60 60"><path d="M8 30l14 14 30-30" fill="none" stroke="#1e8cf0" stroke-width="9" stroke-linecap="round" stroke-linejoin="round"/></svg>
</div>
<div class="abs feature-ring" style="left:535px;top:1631px">
  <svg width="60" height="70" viewBox="0 0 60 70"><path d="M18 40l-8 22 10-5 5 9 6-20zM42 40l8 22-10-5-5 9-6-20z" fill="#1e8cf0"/><circle cx="30" cy="26" r="22" fill="#1e8cf0"/><path d="M30 14l3.5 8 8.5.8-6.5 5.7 2 8.3-7.5-4.4-7.5 4.4 2-8.3-6.5-5.7 8.5-.8z" fill="#fff"/></svg>
</div>
<div class="abs feature-ring" style="left:807px;top:1631px">
  <svg width="56" height="62" viewBox="0 0 56 62" fill="none" stroke="#1e8cf0" stroke-width="3.5"><rect x="6" y="4" width="36" height="50" rx="3"/><line x1="14" y1="16" x2="34" y2="16"/><line x1="14" y1="26" x2="34" y2="26"/><line x1="14" y1="36" x2="28" y2="36"/><circle cx="42" cy="44" r="7" fill="#1e8cf0"/></svg>
</div>
<div class="abs feature-label" style="left:198px;top:1788px">DONE FOR YOU</div>
<div class="abs feature-label" style="left:470px;top:1788px">PREMIUM CONTENT</div>
<div class="abs feature-label" style="left:742px;top:1788px">FULLY LICENSED TO YOU</div>

<!-- row 2 -->
<div class="abs feature-ring" style="left:263px;top:1861px">
  <svg width="64" height="52" viewBox="0 0 64 52"><path d="M6 20h10l22-12v36L16 32H6z" fill="#1e8cf0"/><rect x="12" y="32" width="8" height="14" fill="#1e8cf0"/><g stroke="#1e8cf0" stroke-width="3" stroke-linecap="round"><line x1="46" y1="26" x2="58" y2="26"/><line x1="45" y1="16" x2="55" y2="8"/><line x1="45" y1="36" x2="55" y2="44"/></g></svg>
</div>
<div class="abs feature-ring" style="left:535px;top:1861px">
  <svg width="56" height="56" viewBox="0 0 56 56"><circle cx="28" cy="28" r="24" fill="none" stroke="#1e8cf0" stroke-width="4"/><path d="M22 16l18 12-18 12z" fill="#1e8cf0"/></svg>
</div>
<div class="abs feature-ring" style="left:807px;top:1861px">
  <svg width="56" height="64" viewBox="0 0 56 64"><circle cx="32" cy="22" r="14" fill="none" stroke="#1e8cf0" stroke-width="9" stroke-dasharray="5 4"/><circle cx="32" cy="22" r="9" fill="#1e8cf0"/><circle cx="32" cy="22" r="4" fill="#000"/><circle cx="15" cy="48" r="7" fill="none" stroke="#1e8cf0" stroke-width="5" stroke-dasharray="3 2.5"/></svg>
</div>
<div class="abs feature-label" style="left:198px;top:2018px">PERFECT LENGTH<br>FOR VIDEO ADS</div>
<div class="abs feature-label" style="left:470px;top:2018px">PAGESTREAM VIDEO<br>COVER</div>
<div class="abs feature-label" style="left:742px;top:2018px">BEST SUPPORT</div>

<!-- row 3 -->
<div class="abs feature-ring" style="left:263px;top:2091px">
  <svg width="50" height="64" viewBox="0 0 50 64" fill="none" stroke="#1e8cf0" stroke-width="2"><rect x="14" y="4" width="22" height="56" rx="2"/><path d="M14 12H4v40h10M36 12h10v40H36" stroke-dasharray="3 3"/><path d="M22 28l8 4-8 4z" fill="#1e8cf0"/></svg>
</div>
<div class="abs feature-ring" style="left:535px;top:2091px">
  <svg width="54" height="54" viewBox="0 0 54 54"><rect x="4" y="4" width="46" height="46" fill="none" stroke="#1e8cf0" stroke-width="2.5"/><path d="M22 20l12 7-12 7z" fill="#1e8cf0"/></svg>
</div>
<div class="abs feature-ring" style="left:807px;top:2091px">
  <svg width="84" height="60" viewBox="0 0 84 60"><rect x="2" y="2" width="80" height="56" rx="4" fill="#1e8cf0"/><rect x="6" y="6" width="72" height="48" rx="3" fill="none" stroke="#fff" stroke-width="1.5"/><text x="42" y="28" text-anchor="middle" font-family="Raleway,sans-serif" font-weight="800" font-size="19" fill="#fff">1080p</text><text x="42" y="48" text-anchor="middle" font-family="Raleway,sans-serif" font-weight="600" font-size="15" fill="#fff">FULLHD</text></svg>
</div>
<div class="abs feature-label" style="left:198px;top:2248px">VERTICAL VIDEO<br>FORMAT</div>
<div class="abs feature-label" style="left:470px;top:2248px">SQUARE VIDEO<br>FORMATS</div>
<div class="abs feature-label" style="left:742px;top:2248px">FULL H.D. VIDEO<br>FORMATS</div>

<section class="abs sizes-bg" role="img" aria-label="Swirling collage of floating video screens"></section>
<h2 class="abs center section-title" style="top:2407px">VIDEO SIZES AVAILABLE</h2>
<p class="abs sizes-text" style="top:2495px"><span class="stars">***</span> <b>Wide Screen Videos – This size is a standard video size that works best for pretty much anywhere on the web (1080x720)</b><br>Included with all video purchases</p>
<p class="abs sizes-text" style="top:2568px"><span class="stars">***</span> <b>Square Videos that work best on PAGESTREAM (Square is 1080 X 1080)</b><br>Convert any video to this size for an additional fee of $39</p>
<p class="abs sizes-text" style="top:2622px"><span class="stars">***</span> <b>Vertical Videos that work best on STORIES for Pagestream, Lumigram and Flashtalk (1080 X 1920)</b><br>Convert any video to this size for an additional fee of $39</p>

<div class="abs frame" style="left:234px;top:2690px;width:187px;height:123px">1080<em>x</em>720</div>
<div class="abs frame" style="left:507px;top:2690px;width:187px;height:186px">1080<em>x</em>1080</div>
<div class="abs frame" style="left:778px;top:2690px;width:187px;height:331px">1080<em>x</em>1920</div>

<span class="abs btn small-btn" style="left:522px;top:3054px;width:156px">SEE VIDEOS NOW !</span>

<footer>
  <div class="abs footer-brand">
    <div class="brand-name"><i></i>KELVARA</div>
    <div class="brand-tag" style="font-size:9px">MARKETING VIDEOS MADE FOR YOU</div>
  </div>
  <p class="abs footer-credit">CREATED BY A MARKETER FOR MARKETERS.</p>
  <div class="abs foot-col" style="left:569px">
    <h4>Quick Links</h4>
    <div>Home</div><div>How It Works</div><div>Examples</div><div>FAQ</div><div>Contact Us</div><div>Pricing</div>
  </div>
  <div class="abs foot-col" style="left:708px">
    <h4>About</h4>
    <div>Term Of Service</div><div>Privacy Policy</div><div>Cookies Policy</div>
  </div>
  <div class="abs foot-col" style="left:855px">
    <h4>Follow Us</h4>
    <div class="follow"><span></span><span></span><span></span><span></span><span></span></div>
  </div>
  <p class="abs center copyright">Copyright © 2019 Company Name</p>
</footer>

</body>
</html>
```